your logo, sewn on, your garments ,today , shop

signage

media road side hoarding signs

simple easy to read when driving

be able to read from 100 mtres/yards

see clip hive

amber sail

explains a little what we do here

Target Market(s)

we embroider accross a wide range
from
all types
small business
sports clubs
scouts ,guides
groups
range is very wide

Industry/Entity Type

Shop

Requirements
Must have
• clear information
• be able to understand what we do clearly
• its new to most people so they are confused
• at to whats on offer to sew there logo on there own clothes
• customers are either
• new or existing on our computors
• existing get done faster
• we have a while you wait service
• but the time will take
• depends on amount of work at the time
• and how many logos
• they average 45 minutes each so three logo same garment will be over 2 hours
• so please added on somewhere
• Either
• T & C Apply
• or
• Terms and Conditions Apply
• we have 75,000 customer original logos here that we sew already for customers
• we use road signs 52 weeks of the year to remind people
• a . we are still here
• b .we still have there logos
• c .own garments its new to most of them ?we now can sew on to any of the bargains they can find in sales etc or in the larger supermarkets
Nice to have
• simple logo of a needle thread
Should not have
• should be complicated
• everyone is a individual
• we like them to make there own judgement on there own logos

```html
<!DOCTYPE html>
<html lang="en">
<head>
<meta charset="utf-8">
<title>Amber Sail – Your Logo Sewn On</title>
<link rel="stylesheet" href="https://fonts.googleapis.com/css2?family=Arimo&family=Parisienne&family=Fira+Sans:wght@400;500;800&family=Noto+Sans&display=swap">
<style>
  :root {
    --brand-red: #cf1c24;
    --brand-blue: #302f86;
    --paper: #ffffff;
  }
  * { margin: 0; padding: 0; box-sizing: border-box; }
  html, body { width: 1200px; height: 600px; overflow: hidden; background: var(--paper); }
  .hoarding { position: relative; width: 1200px; height: 600px; background: var(--paper); overflow: hidden; }

  /* Left: logo promise */
  .logo-placeholder {
    position: absolute; left: 167px; top: 15px; width: 126px; height: 126px;
    border-radius: 50%; background: var(--brand-red);
  }
  .logo-caption {
    position: absolute; left: 40px; width: 410px; top: 164px; text-align: center;
    font-family: "Arimo", Arial, sans-serif; font-size: 76px; color: var(--brand-red); line-height: 1;
  }
  .script-word {
    position: absolute; font-family: "Parisienne", cursive; color: var(--brand-blue); line-height: 1;
    white-space: nowrap;
  }
  .script-sewn { left: 108px; top: 262px; font-size: 132px; }
  .script-on { left: 212px; top: 408px; font-size: 140px; }

  /* Centre: garment */
  .garment {
    position: absolute; left: 490px; top: 116px; width: 292px; height: 466px;
    background: var(--brand-red); border-radius: 60px 60px 14px 14px;
  }
  .garment-label {
    position: absolute; left: 632px; top: 352px;
    transform: translate(-50%, -50%) rotate(90deg);
    font-family: "Arimo", Arial, sans-serif; font-size: 66px; color: var(--paper);
    white-space: nowrap; line-height: 1;
  }

  /* Right: brand panel */
  .brand-panel { position: absolute; left: 828px; top: 0; width: 372px; height: 600px; background: var(--paper); }
  .brand-name {
    display: block; text-align: center; font-family: "Arimo", Arial, sans-serif;
    color: var(--paper); line-height: 1; font-size: 80px;
  }
  .brand-name--top { height: 78px; background: var(--brand-red); padding-top: 2px; }
  .brand-name--bottom { height: 80px; background: var(--brand-blue); padding-top: 4px; }
  .offer {
    position: absolute; top: 162px; left: 0; width: 372px; height: 223px;
    background: var(--brand-red); color: var(--paper); text-align: center;
    font-family: "Fira Sans", sans-serif; padding-top: 22px;
  }
  .offer-line { font-size: 28px; font-variant: small-caps; letter-spacing: 1.8px; line-height: 34px; }
  .offer-strong { font-weight: 800; font-size: 39px; line-height: 38px; letter-spacing: 0.5px; }
  .offer-small { font-variant: small-caps; font-size: 24px; line-height: 26px; letter-spacing: 1px; }
  .contact {
    position: absolute; top: 388px; left: 0; width: 372px; height: 212px;
    background: var(--brand-blue); color: var(--paper); text-align: center;
  }
  .contact-email { margin-top: 38px; font-family: "Arimo", Arial, sans-serif; font-size: 27px; }
  .contact-phone { font-family: "Fira Sans", sans-serif; font-weight: 500; font-size: 40px; letter-spacing: 2px; margin-top: 0; line-height: 46px; }
  .contact-address { font-family: "Noto Sans", sans-serif; font-size: 18px; line-height: 30px; margin-top: 20px; letter-spacing: 0.6px; }
</style>
</head>
<body>
<main class="hoarding">
  <div class="logo-placeholder" role="img" aria-label="Space for the customer's logo"></div>
  <p class="logo-caption">Your Logo</p>
  <p class="script-word script-sewn">Sewn</p>
  <p class="script-word script-on">On</p>

  <div class="garment" role="img" aria-label="Red T-shirt silhouette"></div>
  <p class="garment-label">Your Clothes</p>

  <aside class="brand-panel">
    <span class="brand-name brand-name--top">AMBER</span>
    <span class="brand-name brand-name--bottom">SAIL</span>
    <div class="offer">
      <p class="offer-line">We are now able to</p>
      <p class="offer-line">offer embroidering</p>
      <p class="offer-strong">YOUR LOGO</p>
      <p class="offer-small">onto</p>
      <p class="offer-strong">YOUR CLOTHES</p>
    </div>
    <div class="contact">
      <p class="contact-email">sales@ambersail.co.uk</p>
      <p class="contact-phone">01632 9600000</p>
      <p class="contact-address">214 to 220 Marlow Road,<br>Ashby, Westshire AB4 7QZ</p>
    </div>
  </aside>
</main>
</body>
</html>
```